LANDING PAGE on a Word Press platform.

I have a website, www.thequietharborledger.com and need to create a new landing page. I purchased a new url, www.quietharborledger.com and set it up on Word Press. It has a theme (I was trying to do it myself, but gave up) but you can change it if you need to. I will give you access so you can work directly on the Word Press Platform. Please visit my site, www.thequietharborledger, so you can see what we are selling.
Updates

Thank you for being so patient. Unfortunately I had some pressing personal problems and had to leave the country for a couple of weeks. I am back now and will choose a design today. Thank you again!

Target Market(s)

Stock Market, High Worth Individuals, Traders, Investors

Requirements
Must have
• My landing page must look very professional and rich. I am sending a copy of my logo but the "the" before The Quiet Harbor Ledger, needs to be removed. Some testimonials and services we provide. (all found on my home page)
Nice to have
• I am open to a new color scheme if possible. The logo colors would have to be changed.
Should not have
• Should not be too busy with too many images or text. I want a clean and easy to read landing page

```html
<!DOCTYPE html>
<html lang="en">
<head>
<meta charset="utf-8">
<title>The Quiet Harbor Ledger</title>
<link href="https://fonts.googleapis.com/css2?family=Arimo:wght@400;700&family=Open+Sans:wght@400;600;700&display=swap" rel="stylesheet">
<style>
:root{
  --navy:#0d1b4f;
  --navy-deep:#0a1440;
  --blue:#1b5fa0;
  --teal:#2a7bb0;
  --gold:#d4a017;
  --gold-text:#e2a51c;
  --text:#555;
  --white:#fff;
  --rule:#ccc;
}
*{margin:0;padding:0;box-sizing:border-box}
html,body{width:1200px;height:2174px;overflow:hidden;background:var(--white)}
body{position:relative;font-family:"Arimo",Arial,sans-serif;color:var(--text)}
.abs{position:absolute}

.site-header{left:0;top:0;width:1200px;height:116px;border-top:3px solid var(--gold)}
.brand{left:101px;top:20px;display:flex;align-items:center;gap:10px}
.brand-mark{width:72px;height:72px;border-radius:50%;background:var(--blue)}
.brand-name{font-weight:700;font-size:30px;line-height:32px;color:var(--navy);width:190px}
.btn-top{width:128px;height:25px;top:23px;background:linear-gradient(#23407a,var(--navy-deep));color:var(--white);font-weight:700;font-size:13px;text-align:center;line-height:25px}
.contact{top:76px;right:100px;font-size:12px;font-weight:700;color:var(--navy)}
.contact span{color:var(--gold-text)}

.main-nav{left:0;top:116px;width:1200px;height:29px;background:linear-gradient(#2d6ca8,#0f2c66 60%,#0a1d4c);display:flex;justify-content:center}
.main-nav a{color:var(--white);text-decoration:none;font-weight:700;font-size:12.5px;line-height:29px;padding:0 27px;border-right:1px solid rgba(255,255,255,.15)}
.main-nav a.active{color:#f5c542}
.main-nav a:last-child{border:0}

.hero{left:0;top:145px;width:1200px;height:465px;background:
  radial-gradient(ellipse 260px 200px at 660px 180px,rgba(120,160,205,.55),transparent 70%),
  radial-gradient(ellipse 220px 160px at 1000px 260px,rgba(170,185,205,.6),transparent 70%),
  radial-gradient(ellipse 240px 180px at 220px 280px,rgba(215,190,165,.55),transparent 70%),
  linear-gradient(180deg,#eef2f6,#d9e1ea 55%,#b9c4cf)}
.hero-caption{left:0;top:483px;width:1200px;height:127px;background:rgba(35,35,35,.88)}
.hero-caption h2{position:absolute;top:38px;width:100%;text-align:center;font-size:31px;letter-spacing:1.5px;color:var(--white)}
.hero-caption h2 em{font-style:normal;color:var(--teal)}
.dots{left:578px;top:592px;display:flex;gap:6px}
.dots i{width:9px;height:9px;border-radius:50%;background:#ccc}
.dots i.on{background:var(--teal)}

.section-title{width:1200px;left:0;text-align:center;font-size:26px;font-weight:700;color:var(--navy)}
.intro{left:100px;top:708px;width:512px;font-size:12px;line-height:19px}
.intro p+p{margin-top:38px}
.intro-image{left:622px;top:709px;width:478px;height:165px;border:1px solid var(--rule);background:linear-gradient(120deg,#d8dde3,#c79d3a 45%,#7a7f86 70%,#e9e2b8)}

.trades{left:97px;top:991px;width:333px;border:1px solid var(--rule);font-family:"Open Sans",sans-serif;font-size:11px;color:#111}
.trades caption{font-weight:700;font-size:11px;padding:2px 0}
.trades table{width:100%;border-collapse:collapse}
.trades thead th{background:var(--navy);color:var(--white);font-weight:600;font-size:10.5px;line-height:13px;padding:1px 2px;vertical-align:bottom}
.trades td{padding:0 3px;line-height:16px;text-align:right}
.trades td:first-child{text-align:left}
.perf-text{left:445px;top:994px;width:302px;text-align:center;font-size:12px;line-height:19px}
.perf-text p+p{margin-top:19px}
.chart{left:756px;top:991px;width:345px;height:215px;border:1px solid var(--rule)}

.card{top:1327px;width:308px;height:358px;border:1px solid var(--rule);padding:5px}
.card-inner{height:100%;background:radial-gradient(ellipse at 50% 55%,#1d3378,var(--navy-deep) 75%);text-align:center;font-family:"Open Sans",sans-serif;color:var(--white)}
.card h3{padding-top:26px;font-size:15px;font-weight:700;line-height:20px}
.portrait{width:170px;height:170px;margin:12px auto 0;border:4px solid var(--white);background:#8e949b}
.card p{margin:16px 20px 0;font-size:11px;line-height:24px}
.card a{display:block;color:var(--gold-text);font-size:11px;line-height:18px;text-decoration:none}

.cta{left:0;top:1729px;width:1200px;height:221px;background:radial-gradient(ellipse at 70% 60%,#3a3f47,#1d2127 60%,#121418)}
.cta h2{position:absolute;top:62px;width:100%;text-align:center;color:var(--white);font-size:36px;letter-spacing:.5px}
.cta h2 em{font-style:normal;color:var(--teal)}
.cta-btn{left:456px;top:1859px;width:296px;height:51px;background:linear-gradient(#2c76b5,#0f2c66);color:var(--white);font-weight:700;font-size:31px;text-align:center;line-height:51px;box-shadow:0 3px 6px rgba(0,0,0,.5)}

.plan{top:2004px;height:56px;background:linear-gradient(#2c85c2,#1a5e9c);border:2px solid var(--navy);color:var(--navy);font-weight:700;font-size:17px;text-align:center;line-height:22px;padding-top:6px;box-shadow:3px 3px 4px rgba(0,0,0,.35);z-index:2}
.plan b{color:var(--white)}
.plan .price{color:var(--white)}

.site-footer{left:0;top:2060px;width:1200px;height:114px;background:linear-gradient(#2a7bb8,#0f2c66 55%,#0a1440)}
.social{left:497px;top:2059px;display:flex;gap:6px;z-index:2}
.social i{width:28px;height:34px;border:2px solid #cfd6e4}
.foot-links{left:0;top:54px;width:100%;text-align:center;font-size:11px;color:var(--white)}
.foot-links a{color:var(--white);text-decoration:none;margin:0 5px}
.copyright{left:0;top:88px;width:100%;text-align:center;font-size:10px;color:var(--white)}
</style>
</head>
<body>

<header class="site-header abs">
  <div class="brand abs"><span class="brand-mark"></span><span class="brand-name">Quiet Harbor Ledger</span></div>
  <div class="btn-top abs" style="left:822px">SUBSCRIBE</div>
  <div class="btn-top abs" style="left:972px">LOGIN</div>
  <div class="contact abs"><span>E-MAIL :</span> info@thequietharborledger.com &nbsp;&nbsp;&nbsp;&nbsp;&nbsp;<span>PHONE :</span> 555-014-2277</div>
</header>

<nav class="main-nav abs">
  <a class="active">HOME</a><a>ABOUT</a><a>CURRENT PORTFOLIO</a><a>LATEST REPORT</a><a>WATCH LIST</a><a>DAILY TICKER</a><a>MARKET NEWS</a>
</nav>

<div class="hero abs" role="img" aria-label="Team of smiling traders gathered around a laptop in a bright office with charts on the wall"></div>
<div class="hero-caption abs"><h2><em>COMBINING &nbsp;FUNDAMENTAL</em> &nbsp;AND &nbsp;TECHNICAL &nbsp;ANALYSIS</h2></div>
<div class="dots abs"><i></i><i class="on"></i><i></i></div>

<h2 class="section-title abs" style="top:646px">WELCOME TO THE QUIET HARBOR LEDGER</h2>
<div class="intro abs">
  <p>Our Team of Researchers, Stock Traders and Contributors would like to welcome you to "The Quiet Harbor Ledger", an opportunity to receive research and opinions on companies and stocks that will outperform the market!!</p>
  <p>If you are an investor or stock trader looking for high quality investment ideas with strong fundamentals to support them, look no further than the "The Quiet Harbor Ledger" as an invaluable resource of investment information. Our approach combines fundamental and technical analysis in order to introduce fresh and successful ideas to our readers.</p>
</div>
<div class="intro-image abs" role="img" aria-label="Gold bar charts rising over financial papers and a pie chart"></div>

<h2 class="section-title abs" style="top:930px">TOP TEN TRADES &amp; PERFORMANCE</h2>
<div class="trades abs">
  <table>
    <caption>TQHL TOP TEN TRADES OF Q1 2015</caption>
    <thead><tr><th style="text-align:left">Ticker</th><th>Purchase Date</th><th>Purchase Price</th><th>Best Price Since Entry</th><th>Return</th><th>High Date</th></tr></thead>
    <tbody>
      <tr><td>KELP</td><td>2/4/2015</td><td>3.75</td><td>11.00</td><td>193%</td><td>2/27/2015</td></tr>
      <tr><td>ORBT</td><td>2/24/2015</td><td>10.75</td><td>$19.63</td><td>83%</td><td>3/5/2015</td></tr>
      <tr><td>VANT</td><td>2/11/2015</td><td>$40.50</td><td>70.48</td><td>74%</td><td>2/20/2015</td></tr>
      <tr><td>MRLN</td><td>1/26/2015</td><td>8.35</td><td>$14.40</td><td>72%</td><td>3/20/2015</td></tr>
      <tr><td>HALO</td><td>2/19/2015</td><td>6.00</td><td>$9.90</td><td>65%</td><td>3/4/2015</td></tr>
      <tr><td>PETL</td><td>2/2/2015</td><td>$8.55</td><td>$13.46</td><td>57%</td><td>3/12/2015</td></tr>
      <tr><td>QUIL</td><td>1/20/2015</td><td>$9.50</td><td>$14.30</td><td>51%</td><td>3/20/2015</td></tr>
      <tr><td>TARN</td><td>2/5/2015</td><td>1.60</td><td>2.26</td><td>41%</td><td>2/24/2015</td></tr>
      <tr><td>BRIO</td><td>3/20/2015</td><td>$5.65</td><td>7.86</td><td>39%</td><td>3/25/2015</td></tr>
      <tr><td>WREN</td><td>1/6/2015</td><td>$38.25</td><td>$51.87</td><td>36%</td><td>3/25/2015</td></tr>
    </tbody>
  </table>
</div>
<div class="perf-text abs">
  <p>In the first quarter of 2015, the top ten recommendations had an average return of 74% with KELP generating the highest return of 193%.</p>
  <p>In 2015, TQHL's Tweets and Current Portfolio generated combined profits of $70,847.</p>
  <p>In the first quarter of 2015, including open trades, TQHL's Current Portfolio had 56 recommendations for a total profit of $23,412. The 56 recommendations had 33 positive trades for a win ratio of 59%.</p>
</div>
<svg class="chart abs" viewBox="0 0 345 215" font-family="Open Sans, sans-serif">
  <text x="172" y="16" text-anchor="middle" font-size="10" font-weight="700" fill="#111">Performance of TQHL Portfolios vs. Major Indices</text>
  <g font-size="6" fill="#333">
    <text x="4" y="10">155</text><text x="4" y="40">145</text><text x="4" y="60">135</text><text x="4" y="83">125</text><text x="4" y="106">115</text><text x="4" y="129">105</text><text x="4" y="152">95</text>
  </g>
  <line x1="20" y1="150" x2="335" y2="150" stroke="#999" stroke-width=".6"/>
  <polyline fill="none" stroke="#c0392b" stroke-width="1.6" points="22,142 45,138 70,133 90,130 110,126 130,120 150,112 170,100 185,92 200,84 215,70 225,55 235,50 245,25 258,30 270,36 285,32 300,30 315,25 330,20"/>
  <polyline fill="none" stroke="#1d2e6b" stroke-width="1.6" points="22,142 45,140 60,146 80,138 100,143 120,135 140,128 160,126 180,122 200,116 220,114 240,110 260,112 280,108 300,110 315,106 330,112"/>
  <polyline fill="none" stroke="#888" stroke-width="1.2" points="22,142 50,143 80,141 110,140 140,138 170,134 200,133 230,132 260,130 290,132 330,130"/>
  <polyline fill="none" stroke="#8e8ec8" stroke-width="1.2" points="22,142 50,145 80,142 110,141 140,137 170,133 200,130 230,128 260,130 290,127 330,129"/>
  <polyline fill="none" stroke="#111" stroke-width="1.2" points="22,142 50,146 80,140 110,138 140,134 170,130 200,126 230,124 260,126 290,123 330,124"/>
  <g font-size="5.5" fill="#333">
    <text transform="translate(26,178) rotate(-60)">1/2/2015</text><text transform="translate(60,178) rotate(-60)">1/9/2015</text><text transform="translate(94,178) rotate(-60)">1/16/2015</text><text transform="translate(128,178) rotate(-60)">1/23/2015</text><text transform="translate(162,178) rotate(-60)">1/30/2015</text><text transform="translate(196,178) rotate(-60)">2/6/2015</text><text transform="translate(230,178) rotate(-60)">2/13/2015</text><text transform="translate(264,178) rotate(-60)">2/20/2015</text><text transform="translate(298,178) rotate(-60)">3/6/2015</text><text transform="translate(330,178) rotate(-60)">3/13/2015</text>
  </g>
  <g font-size="6" fill="#333">
    <line x1="30" y1="204" x2="42" y2="204" stroke="#1d2e6b" stroke-width="1.5"/><text x="45" y="206">Current Portfolio</text>
    <line x1="100" y1="204" x2="112" y2="204" stroke="#c0392b" stroke-width="1.5"/><text x="115" y="206">Tweeted Trades</text>
    <line x1="165" y1="204" x2="177" y2="204" stroke="#888" stroke-width="1.5"/><text x="180" y="206">Broad 500</text>
    <line x1="215" y1="204" x2="227" y2="204" stroke="#8e8ec8" stroke-width="1.5"/><text x="230" y="206">Industrials</text>
    <line x1="265" y1="204" x2="277" y2="204" stroke="#111" stroke-width="1.5"/><text x="280" y="206">Tech Index</text>
  </g>
</svg>

<h2 class="section-title abs" style="top:1256px">OUR TEAM MANAGEMENT</h2>
<article class="card abs" style="left:99px"><div class="card-inner">
  <h3>WARREN KESSLER</h3><div class="portrait" role="img" aria-label="Portrait of the managing editor"></div>
  <p>Mr. Kessler is the Managing Editor and Founder of TQHL Publishing (parent company to The Quiet Harbor Ledger)</p><a>Read more &gt;&gt;</a>
</div></article>
<article class="card abs" style="left:447px"><div class="card-inner">
  <h3>LEON MARSH</h3><div class="portrait" role="img" aria-label="Portrait of the technical analyst"></div>
  <p>Leon Marsh has more than 40 years of Wall Street investment and technical analysis experience.</p><a>Read more &gt;&gt;</a>
</div></article>
<article class="card abs" style="left:793px"><div class="card-inner">
  <h3>DALE WHITFORD</h3><div class="portrait" role="img" aria-label="Portrait of the contributor"></div>
  <p>Born, raised and educated in Upstate New York, Dale Whitford began investing at the age of 18. This started as an .</p><a>Read more &gt;&gt;</a>
</div></article>

<section class="cta abs" role="img" aria-label="Dim background of blurred financial charts">
  <h2><em>SUBSCRIBE NOW</em> : START A 2 WEEK REFF TRIAL TODAY</h2>
</section>
<div class="cta-btn abs">SUBSCRIBE</div>

<div class="plan abs" style="left:98px;width:210px">FREE <b>2</b> WEEK<br>TRIAL</div>
<div class="plan abs" style="left:894px;width:207px">MONTHLY PAID<br><span class="price">$150.00</span></div>

<footer class="site-footer abs">
  <div class="foot-links abs"><a>HOME</a><a>ABOUT</a><a>CURRENT PORTFOLIO</a><a>LATEST REPORT</a><a>WATCHLIST</a><a>DAILY TICKER</a><a>MARKET NEWS</a><a>DISCLAIMER</a></div>
  <div class="copyright abs">©Copyright 2015 The Quiet Harbor Ledger.</div>
</footer>
<div class="social abs">
  <i style="background:#2b4a8a"></i><i style="background:#2d86c4"></i><i style="background:#b0242c"></i><i style="background:#d9821e"></i><i style="background:#3b5c46"></i><i style="background:#1f6e9c"></i>
</div>

</body>
</html>
```